Four Quiet Steps Toward a Stronger Offer on THE Property - VARN Real Estate

I have written an E-Book that is called "Four Quiet Steps Toward a Stronger Offer on The Property." The E-Book will be available as a FREE download from my VARN Real Estate landing page, and also from a Chatterbox campaign that will be commencing in early September.

The E-Book content is in the WORD document below - I now need for it to be made to look more professional and suitable for publishing and placed on my landing page for download. Please review and send me some proposals for this e-book to be a bit more eye catching and appealing than just a WORD doc.

My VARN Real Estate landing page is still under development and you can see the what is close to the final proposal here:

http://www.plum-orbit.com.au/varn/

The cover of the E-Book is at the bottom of the page. Please review and give the internals the sale look and feel.

Target Market(s)

Home and Property Owners in the middle ring Eastern Suburbs of Melbourne - approximately 15 - 30 km's from the central business district. The area is a very family oriented area and features mostly houses that are 3 or 4 bedroom - with some larger properties that are five or more bedrooms. The area is quite an expensive suburban community and house prices range between the low of $1,000,000 to a high of more than $2,500,000. The predominant cultural group that buys in this area are Chinese and Chinese Australian buyers. The predominant group who are selling are usually Australians of a white anglo-saxon background. Other groups are of Asian sub continent background (Indian / Sri Lankan/ Pakistan). All are families that are attracted to the area because of the great schools, good shopping, leisure facilities (parks, pools, courts etc), and excellent public and road transport infrastructure. Read the content of my e-book - it tells you every thing you need to know :)

Industry/Entity Type

Real Estate

Colors

Designer to choose colors to be used in the design.

Requirements
Must have
• Once completed the layout should not be too busy - it should be easy to read. I guess then the statement "less is more" is applicable.
• I will probably print a number of copies of this book for distribution as well - so please consider print attributes in the design.
• IMPORTANT: as for any e-book offering specialist advice, the MAIN reason for the book is for the generation of sales leads and to establish the author as a subject matter expert on the topic. Please consider this in your design elements. BUT - the book should also not come across as 1 big advertisement either. Subtle but impactful are well chosen words to describe how it should present.
Nice to have
• VARN Real Estate branding on every page - to re-inforce the message.
Should not have
• No need for animations or illustrations/

```html
<!DOCTYPE html>
<html lang="en">
<head>
<meta charset="utf-8">
<title>VARN Real Estate – E-Book Pages</title>
<link href="https://fonts.googleapis.com/css2?family=Oswald:wght@500&family=Open+Sans:ital,wght@0,400;0,600;0,700;0,800;1,400&family=Nunito:wght@700&display=swap" rel="stylesheet">
<style>
:root{
  --teal:#3dbb95;
  --ink:#2b2b2b;
  --black:#101010;
  --text:#3a3a3a;
  --paper:#ffffff;
  --stage:#e7e4df;
  --roof:#242424;
}
*{box-sizing:border-box;margin:0;padding:0}
html,body{width:1200px;height:1200px;overflow:hidden}
body{background:var(--stage);font-family:"Open Sans",Arial,sans-serif;color:var(--text)}
.spread{position:absolute;top:204px;left:25px;width:1150px;height:792px}
.page{position:absolute;top:0;width:560px;height:792px;background:var(--paper);box-shadow:0 6px 18px rgba(0,0,0,.18);overflow:hidden}
.page--one{left:0}
.page--two{left:590px}
.hero{position:absolute;left:0;top:0;width:560px;height:312px}
.brand{position:absolute;right:34px;top:30px;text-align:right}
.brand__name{font-family:"Open Sans",Arial,sans-serif;font-weight:800;font-size:56px;line-height:50px;color:var(--ink);letter-spacing:-1px}
.brand__sub{font-size:8.5px;letter-spacing:11.2px;color:var(--ink);margin-top:6px;margin-right:-10px}
.hero__title{position:absolute;left:62px;top:92px;font-family:"Nunito",sans-serif;font-weight:700;font-size:21px;line-height:27px;color:#fff;text-shadow:0 1px 3px rgba(0,0,0,.35)}
.hero__title span{display:block}
.hero__title span:first-child{margin-left:26px}
.heading{position:absolute;left:34px;top:326px;font-family:"Oswald",sans-serif;font-weight:500;font-size:15px;color:var(--teal);letter-spacing:.3px;text-transform:uppercase}
.body{font-size:7.4px;line-height:10px;text-align:justify}
.body p+p{margin-top:8px}
.intro{position:absolute;left:34px;right:34px;top:352px}
.location{position:absolute;left:0;top:449px;width:560px;height:236px;background:var(--black);color:#eaeaea;padding:11px 34px 0}
.location__title{font-size:11.6px;color:var(--teal);font-weight:400}
.location__lead{font-size:7.4px;line-height:10px;margin-top:10px}
.features{display:flex;gap:16px;margin-top:12px}
.features ul{list-style:none;flex:1}
.features li{position:relative;padding-left:15px;font-size:7.4px;line-height:10px;text-align:justify;margin-bottom:10px}
.features li svg{position:absolute;left:0;top:1px;width:10px;height:10px}
.hl{color:var(--teal)}
.outro{position:absolute;left:34px;right:34px;top:697px}
.footer{position:absolute;left:0;top:740px;width:560px;height:40px}
.footer__url{position:absolute;left:0;width:420px;top:8px;text-align:center;font-size:8px;letter-spacing:2.6px;color:#fff}
.footer__num{position:absolute;right:18px;top:7px;font-family:"Open Sans",sans-serif;font-size:18px;color:var(--teal)}
.cols{position:absolute;left:34px;right:34px;display:flex;gap:20px}
.cols>div{flex:1}
.cols--top{top:352px}
.cols strong{font-weight:700;color:#111}
.quote{position:absolute;left:34px;right:34px;top:450px;height:70px}
.quote p{position:absolute;left:0;right:0;top:22px;font-style:italic;font-size:7.2px;line-height:10px;color:#222}
.body--wide{position:absolute;left:34px;right:34px;top:530px}
.subhead{position:absolute;left:34px;top:624px;font-family:"Oswald",sans-serif;font-weight:500;font-size:12.5px;color:#222;text-transform:none}
.pill{position:absolute;left:0;top:647px;width:117px;height:14px;background:var(--teal);border-radius:0 8px 8px 0;color:#fff;font-size:8.4px;line-height:14px;padding-left:34px}
.cols--basics{top:664px}
.cols--basics .right{margin-top:-40px}
</style>
</head>
<body>
<div class="spread">

  <section class="page page--one">
    <div class="hero">
      <svg width="560" height="312" viewBox="0 0 560 312">
        <defs>
          <linearGradient id="sky1" x1="0" y1="0" x2="0" y2="1">
            <stop offset="0" stop-color="#1d4f9e"/>
            <stop offset=".45" stop-color="#5f8fd0"/>
            <stop offset=".6" stop-color="#8a7a6a"/>
            <stop offset=".8" stop-color="#4c7a3a"/>
            <stop offset="1" stop-color="#6aa548"/>
          </linearGradient>
        </defs>
        <g role="img" aria-label="Photo of a brick family home with garden under a blue sky">
          <polygon points="39,116 170,44 294,116" fill="#1d4f9e"/>
          <rect x="0" y="112" width="560" height="200" fill="url(#sky1)"/>
        </g>
        <polyline points="0,112 39,112 170,42 294,112 560,112" fill="none" stroke="var(--roof)" stroke-width="5" stroke-linejoin="miter"/>
        <polygon points="44,110 170,44 290,110 290,116 44,116" fill="#1d4f9e"/>
        <line x1="0" y1="311" x2="560" y2="311" stroke="#fff" stroke-width="2"/>
      </svg>
      <div class="brand">
        <div class="brand__name">VARN</div>
        <div class="brand__sub">REAL ESTATE</div>
      </div>
      <div class="hero__title"><span>City of Ashvale</span><span>&amp; City of Greymere</span></div>
    </div>

    <h1 class="heading">Four Quiet Steps Toward a Stronger Offer on The Property</h1>

    <div class="intro body">
      <p>So after much consideration you have made the decision to sell your property. For some of you the home may have held many long and happy memories. For others it may have been a property used purely as an investment vehicle to greater wealth. Unfortunately for some others it may be necessary to sell due to life challenges – these may be financial issues, a marriage breakdown or even the passing away of a relative. Whatever the reason and your motivation for selling – once the decision to sell is made, the most important end result is to get for your property the best possible price available in the market place.</p>
      <p>In my free e-book – you will find Four Quiet Steps Toward a Stronger Offer on The Property. It includes some useful tips to help you prepare your property to be put on the market for sale. Then once it is ready – what to do to extract top dollar for the sale of your home.</p>
    </div>

    <div class="location">
      <h2 class="location__title">By the way....CONGRATULATIONS on your choice of location:</h2>
      <p class="location__lead">The desirable and leafy City of Ashvale and City of Greymere are exceptionally popular residential localities – and it is little wonder when you consider all that they offer to the modern family. The standout features of these two great municipalities include:</p>
      <div class="features">
        <ul>
          <li><svg viewBox="0 0 10 10"><circle cx="5" cy="5" r="4.3" fill="none" stroke="var(--teal)" stroke-width="1"/><path d="M3 5.2l1.5 1.5L7.2 3.8" fill="none" stroke="var(--teal)" stroke-width="1.1"/></svg><span class="hl">Superb education options</span> – some of Melbourne's leading government and private primary and secondary schools are located within the boundaries of the City of Ashvale and the City of Greymere. There are also excellent tertiary education choices present with Corran University (Burwood campus), Ashvale University (Clayton campus), Fernbrook Institute, and the State Police Academy, amongst others handily located in the region. And the range of great childcare and Kindergarten options round out an amazing list of K-12 education options and beyond for local residents.</li>
          <li><svg viewBox="0 0 10 10"><circle cx="5" cy="5" r="4.3" fill="none" stroke="var(--teal)" stroke-width="1"/><path d="M3 5.2l1.5 1.5L7.2 3.8" fill="none" stroke="var(--teal)" stroke-width="1.1"/></svg><span class="hl">Outstanding shopping</span> exists and includes shopping centres like The Arcade, Hillside Village, Cedar Village, Brookton Park, Woodhill Chase, Boxley Central as well as a number of smaller strip shopping and local centres.</li>
        </ul>
        <ul>
          <li><svg viewBox="0 0 10 10"><circle cx="5" cy="5" r="4.3" fill="none" stroke="var(--teal)" stroke-width="1"/><path d="M3 5.2l1.5 1.5L7.2 3.8" fill="none" stroke="var(--teal)" stroke-width="1.1"/></svg><span class="hl">Beautiful parks, gardens, trails and outdoor leisure facilities</span> including Tallow Park, Brook Reserve, Reedmoor Lake Sanctuary, Pipers Creek Trail, Hollins Golf Club, Ridgeway Golf Course, Glenmore Public Golf Course and many other sporting facilities and grounds.</li>
          <li><svg viewBox="0 0 10 10"><circle cx="5" cy="5" r="4.3" fill="none" stroke="var(--teal)" stroke-width="1"/><path d="M3 5.2l1.5 1.5L7.2 3.8" fill="none" stroke="var(--teal)" stroke-width="1.1"/></svg>A large number of <span class="hl">public transport choices</span> for commuters and students spread right across the region including trains, trams and buses depending on your location.</li>
          <li><svg viewBox="0 0 10 10"><circle cx="5" cy="5" r="4.3" fill="none" stroke="var(--teal)" stroke-width="1"/><path d="M3 5.2l1.5 1.5L7.2 3.8" fill="none" stroke="var(--teal)" stroke-width="1.1"/></svg><span class="hl">Excellent freeway and road infrastructure</span> that is continuously evolving and includes the Eastern Ring Freeway, Linkway, and the Northern Freeway. All parts of Melbourne are easily accessible from the City of Ashvale and the City of Greymere.</li>
        </ul>
      </div>
    </div>

    <div class="outro body">
      <p>Education, shopping convenience, leisure facilities and transport infrastructure form the back bone of any desirable community – and the attraction of families, investors and developers to these popular and well established residential areas ensure that the foundation for interest in your property is already in place. So in order for your home to sell well and achieve the best possible price, here are the Four Quiet Steps Toward a Stronger Offer on The Property to help you on your journey.</p>
    </div>

    <div class="footer">
      <svg width="560" height="40" viewBox="0 0 560 40">
        <rect x="0" y="3" width="500" height="20" fill="var(--teal)"/>
        <path d="M486 23 C496 23 498 3 510 3 L560 3 L560 23 Z" fill="var(--ink)"/>
        <rect x="0" y="23" width="560" height="11" fill="var(--ink)"/>
      </svg>
      <div class="footer__url">www.plum-orbit.com.au</div>
      <div class="footer__num">01</div>
    </div>
  </section>

  <section class="page page--two">
    <div class="hero">
      <svg width="560" height="312" viewBox="0 0 560 312">
        <defs>
          <linearGradient id="sky2" x1="0" y1="0" x2="0" y2="1">
            <stop offset="0" stop-color="#3c67ad"/>
            <stop offset=".3" stop-color="#8fb0d9"/>
            <stop offset=".5" stop-color="#9a948a"/>
            <stop offset=".85" stop-color="#7d756c"/>
            <stop offset="1" stop-color="#5c5650"/>
          </linearGradient>
        </defs>
        <g role="img" aria-label="Photo of a modern two-storey rendered home">
          <rect x="0" y="112" width="560" height="200" fill="url(#sky2)"/>
        </g>
        <polyline points="0,112 39,112 170,42 294,112 560,112" fill="none" stroke="var(--roof)" stroke-width="5"/>
        <line x1="0" y1="311" x2="560" y2="311" stroke="#fff" stroke-width="2"/>
      </svg>
      <div class="brand">
        <div class="brand__name">VARN</div>
        <div class="brand__sub">REAL ESTATE</div>
      </div>
    </div>

    <h1 class="heading">1. Property Presentation:</h1>

    <div class="cols cols--top body">
      <div>
        <p><strong>Like any product</strong> – the newer, the cleaner, the shinier, and the better presented a property is for sale...then the more interest it will attract from prospective Buyers.<br>The more Buyer interest that a property attracts...the more competition around the purchase price that will be created.<br>And Buyer competition is fantastic if you know how to harness it to achieve the best possible sale price. But where is it that you should begin and how?</p>
      </div>
      <div>
        <p><strong>So let's start at the very beginning</strong> – property preparation and presentation for sale.<br>It is important to state that very few people actually live in the manner that a house is presented for sale. In most instances what you see at homes that are open for Buyer inspection is the end result of a lot of hard work on behalf of the Vendor and others.<br>So don't be concerned – how ever and whatever your home looks like now...it can be transformed to maximize its appeal to Buyers.</p>
      </div>
    </div>

    <div class="quote">
      <svg width="492" height="70" viewBox="0 0 492 70">
        <circle cx="10" cy="10" r="9" fill="none" stroke="var(--teal)" stroke-width="1.4"/>
        <text x="10" y="18" text-anchor="middle" font-family="Open Sans, sans-serif" font-weight="800" font-size="14" fill="var(--teal)">“</text>
        <line x1="22" y1="10" x2="492" y2="10" stroke="#555" stroke-width=".8"/>
        <line x1="0" y1="58" x2="470" y2="58" stroke="#555" stroke-width=".8"/>
        <circle cx="482" cy="58" r="9" fill="none" stroke="var(--teal)" stroke-width="1.4"/>
        <text x="482" y="66" text-anchor="middle" font-family="Open Sans, sans-serif" font-weight="800" font-size="14" fill="var(--teal)">”</text>
      </svg>
      <p>Vendor's will always see all of the great and wonderful aspects of their property in an effort to create value and push up the price; a Buyer will always tell you everything that is wrong in an effort to drive down the price."</p>
    </div>

    <div class="body--wide body">
      <p>The whole process of buying and selling property is very psychological and highly emotional for most people, so it is very important for Vendors to place themselves in the shoes of a Buyer when running a critical eye across the presentation preparations.</p>
      <p>Your property should be polished, displayed and presented to the highest possible standard. That standard will be different for everyone – factoring in age, ability, financial capacity, the size of family, number of pets and so on.</p>
      <p>In addition - every property is different, and every property has it's own features and personality – what's important is to amplify the positives and minimize the impact of the negatives throughout the home.</p>
    </div>

    <h2 class="subhead">Let's look at some of the basics:</h2>
    <div class="pill">Curbside appeal</div>

    <div class="cols cols--basics body">
      <div>
        <p>First impressions count - stand outside at the front of your house on the street and look at your house with a critical eye. Does your home stand out as a welcoming and "happy" place to arrive at?</p>
        <p>Tidy the gardens, mow the lawns, repair the gutters, paint under the eaves of the roof, clean the windows, repair the cracks in the</p>
      </div>
      <div class="right">
        <p>cement driveways and do some basic landscaping such as adding mulch to garden beds (my personal preference for mulch is black tan bark – but other varieties are just as effective). You will find all these tasks make a huge difference to the exterior look and feel of your property.</p>
        <p>If your property has a fence, then clean it and paint it. Cut back any overgrown trees and bushes, trim and shape the edges of pathways, and clear and remove all rubbish (including rubbish bins) from the front of the house.</p>
      </div>
    </div>

    <div class="footer">
      <svg width="560" height="40" viewBox="0 0 560 40">
        <rect x="0" y="3" width="500" height="20" fill="var(--teal)"/>
        <path d="M486 23 C496 23 498 3 510 3 L560 3 L560 23 Z" fill="var(--ink)"/>
        <rect x="0" y="23" width="560" height="11" fill="var(--ink)"/>
      </svg>
      <div class="footer__url">www.plum-orbit.com.au</div>
      <div class="footer__num">02</div>
    </div>
  </section>

</div>
</body>
</html>
```